Business cards for education company

We need a business card design for a relatively new company based in Queensland and operating across Australia. We resell diploma level education courses which include Business, Management, Finance, Community Services & Government courses. We offer over 20 different courses.
The target market is for anyone 16 years of age and older. There is no age limit.

We would like to see the design use the color blue and silver. The final design should communicate professionalism and a bright future.

We sell education but are also promoting the career they see themselves in 2-3 years in the future

Our company logo is attached.

Target Market(s)

We target all age groups above 16 years of age. The main target market would be people aged between 17-35.

We focus on those people who cannot make it into University or do not want to commit the time to a full degree.

Industry/Entity Type

Education

Requirements
Must have
• Professional
Company logo
website
Contact details:

Please use the following example:

Lionel Parfitt
Senior Education Consultant
0417 386 591
Lionel.parfitt@brightwaylearninghub.com.au
www.brightwaylearninghub.com.au

```html
<!DOCTYPE html>
<html lang="en">
<head>
<meta charset="utf-8">
<title>Brightway Learning Hub – Business Card</title>
<link rel="stylesheet" href="https://fonts.googleapis.com/css2?family=Cabin:wght@400;600&display=swap">
<style>
  :root {
    --card-bg: #ffffff;
    --brand-blue: #1f2ee6;
    --brand-navy: #1b2f7e;
    --accent-circle: #2f8ee8;
    --silver-text: #9aa4b2;
    --chevron-blue: #a3acf9;
    --chevron-silver: #f4f5f8;
  }
  * { margin: 0; padding: 0; box-sizing: border-box; }
  html, body {
    width: 1200px;
    height: 741px;
    overflow: hidden;
    background: var(--card-bg);
  }
  .card {
    position: relative;
    width: 1200px;
    height: 741px;
    background: var(--card-bg);
    font-family: "Cabin", "Gill Sans", sans-serif;
    overflow: hidden;
  }
  .chevrons {
    position: absolute;
    inset: 0;
    width: 1200px;
    height: 741px;
  }
  .chevron-silver { fill: var(--chevron-silver); }
  .chevron-blue { fill: var(--chevron-blue); }

  .brand {
    position: absolute;
    left: 92px;
    top: 120px;
    display: flex;
    align-items: center;
    gap: 18px;
  }
  .brand-mark {
    width: 46px;
    height: 46px;
    border-radius: 50%;
    background: var(--accent-circle);
  }
  .brand-name {
    font-size: 34px;
    font-weight: 600;
    letter-spacing: 1px;
    color: var(--brand-navy);
    line-height: 1;
  }

  .identity {
    position: absolute;
    left: 617px;
    top: 330px;
    transform: translateX(-50%);
    text-align: center;
    white-space: nowrap;
  }
  .identity-name {
    font-size: 40px;
    font-weight: 400;
    color: var(--brand-blue);
    line-height: 48px;
  }
  .identity-role {
    font-size: 34px;
    font-weight: 400;
    color: var(--silver-text);
    line-height: 50px;
  }

  .contact {
    position: absolute;
    left: 90px;
    top: 536px;
    list-style: none;
    font-size: 31px;
    color: var(--brand-blue);
    line-height: 43px;
    white-space: nowrap;
  }
</style>
</head>
<body>
  <div class="card">
    <svg class="chevrons" viewBox="0 0 1200 741" aria-hidden="true">
      <polygon class="chevron-silver" points="644,91 745,91 863,378 745,660 644,660 764,378"/>
      <polygon class="chevron-silver" points="897,91 996,91 1112,378 996,660 897,660 1012,378"/>
      <polygon class="chevron-blue" points="769,91 870,91 984,378 870,660 769,660 885,378"/>
    </svg>

    <div class="brand">
      <span class="brand-mark"></span>
      <span class="brand-name">BRIGHTWAY LEARNING HUB</span>
    </div>

    <div class="identity">
      <p class="identity-name">Lionel Parfitt</p>
      <p class="identity-role">Senior Education Consultant</p>
    </div>

    <ul class="contact">
      <li class="contact-phone">Tel: 0417 386 591</li>
      <li class="contact-email">Email: Lionel.parfitt@brightwaylearninghub.com.au</li>
      <li class="contact-web">www.brightwaylearninghub.com.au</li>
    </ul>
  </div>
</body>
</html>
```